Business Card Design for for an Metallurgical Company

##### ABOUT THE COMPANY #####

TORVANTE is a metallurgical company that manufactures grilles, gates, picket fences, iron boxes, doors, windows, iron bars and other metallurgical processes and services.

##### LOGO ATTACHED #####

##### DATA INFO #####

Name:
- Adriano K. Valmorena

- Position:
Diretor Comercial

- E-mail:
adriano@torvante.com.br

- Company Phone Numbers:
(49) 3291-5873

- Cel Phone Number:
(49) 8576-1937

- Company Address:
Rua Jabuticaba, 518 - Vilanova - Serra Azul/SC - CEP: 89.241-315

- Website:
www.torvante.com.br

```html
<!DOCTYPE html>
<html lang="pt-BR">
<head>
<meta charset="UTF-8">
<title>TORVANTE – Cartão de Visita</title>
<link rel="stylesheet" href="https://fonts.googleapis.com/css2?family=Arimo:wght@400;700&display=swap">
<style>
  :root {
    --stage: #2b2b2b;
    --paper: #f4f4f2;
    --orange: #e8661f;
    --graphite: #3d3d3d;
    --muted: #6a6a6a;
    --font: "Arimo", Arial, sans-serif;
  }
  * { box-sizing: border-box; margin: 0; padding: 0; }
  html, body { width: 1200px; height: 768px; overflow: hidden; }
  body {
    background: var(--stage);
    font-family: var(--font);
    display: flex;
    align-items: center;
    justify-content: center;
    gap: 60px;
  }
  .card {
    width: 520px;
    height: 298px;
    background: var(--paper);
    box-shadow: 0 10px 30px rgba(0,0,0,.45);
    position: relative;
  }
  /* contact side */
  .card--contact {
    border: 9px solid var(--orange);
    display: flex;
    align-items: center;
    padding: 0 26px 0 40px;
  }
  .brand-mark {
    display: flex;
    align-items: center;
    gap: 8px;
    width: 190px;
    color: var(--orange);
    font-weight: 700;
    font-size: 24px;
    letter-spacing: 1px;
  }
  .brand-mark__dot {
    width: 16px; height: 16px;
    border-radius: 50%;
    background: var(--orange);
    flex: none;
  }
  .contact-list { list-style: none; flex: 1; }
  .contact-list li {
    display: flex;
    align-items: flex-start;
    gap: 10px;
    font-size: 11.5px;
    color: var(--muted);
    line-height: 1.3;
    margin-bottom: 9px;
  }
  .contact-list li:last-child { margin-bottom: 0; }
  .contact-list svg {
    width: 13px; height: 13px; flex: none; margin-top: 1px;
    fill: none; stroke: var(--graphite); stroke-width: 1.6;
    stroke-linecap: round; stroke-linejoin: round;
  }
  .person { margin-bottom: 16px !important; }
  .person__name { color: var(--orange); font-weight: 700; font-size: 14px; }
  .person__role { color: var(--graphite); font-weight: 700; font-size: 11px; }
  /* brand side */
  .card--brand {
    display: flex;
    align-items: center;
    justify-content: center;
  }
  .brand-lockup { display: flex; align-items: center; gap: 14px; }
  .brand-lockup__dot {
    width: 44px; height: 44px;
    border-radius: 50%;
    background: var(--orange);
    flex: none;
  }
  .brand-lockup__name {
    color: var(--graphite);
    font-weight: 700;
    font-size: 40px;
    letter-spacing: 3px;
    line-height: 1;
  }
  .brand-lockup__tagline {
    color: var(--muted);
    font-size: 10px;
    letter-spacing: 2.6px;
    margin-top: 5px;
  }
</style>
</head>
<body>

  <section class="card card--contact">
    <div class="brand-mark"><span class="brand-mark__dot"></span>TORVANTE</div>
    <ul class="contact-list">
      <li class="person">
        <svg viewBox="0 0 14 14"><circle cx="7" cy="4.5" r="2.6"/><path d="M2 13c0-3 2.3-4.8 5-4.8s5 1.8 5 4.8"/></svg>
        <div><div class="person__name">Adriano K. Valmorena</div><div class="person__role">Diretor Comercial</div></div>
      </li>
      <li>
        <svg viewBox="0 0 14 14"><rect x="1.5" y="3" width="11" height="8" rx="1"/><path d="M1.5 3.5 7 8l5.5-4.5"/></svg>
        adriano@torvante.com.br
      </li>
      <li>
        <svg viewBox="0 0 14 14"><path d="M3 1.8h2l1 3-1.4 1a7 7 0 0 0 3.6 3.6l1-1.4 3 1v2a1.2 1.2 0 0 1-1.3 1.2A10.5 10.5 0 0 1 1.8 3.1 1.2 1.2 0 0 1 3 1.8z"/></svg>
        (49) 3291-5873
      </li>
      <li>
        <svg viewBox="0 0 14 14"><rect x="3.5" y="1" width="7" height="12" rx="1.2"/><path d="M6.2 11h1.6"/></svg>
        (49) 8576-1937
      </li>
      <li>
        <svg viewBox="0 0 14 14"><path d="M7 13s4.5-4.4 4.5-7.5a4.5 4.5 0 0 0-9 0C2.5 8.6 7 13 7 13z"/><circle cx="7" cy="5.5" r="1.6"/></svg>
        <span>Rua Jabuticaba, 518 - Vilanova<br>Serra Azul/SC - CEP: 89.241-315</span>
      </li>
      <li>
        <svg viewBox="0 0 14 14"><circle cx="7" cy="7" r="5.5"/><path d="M1.5 7h11M7 1.5c2 2 2 9 0 11M7 1.5c-2 2-2 9 0 11"/></svg>
        www.torvante.com.br
      </li>
    </ul>
  </section>

  <section class="card card--brand">
    <div class="brand-lockup">
      <span class="brand-lockup__dot"></span>
      <div>
        <div class="brand-lockup__name">TORVANTE</div>
        <div class="brand-lockup__tagline">SOLUÇÕES EM SERRALHERIA E AÇO</div>
      </div>
    </div>
  </section>

</body>
</html>
```